Landing Page for Church Launch

We are a new Christian Church Plant in Milwaukee Wisconsin. I would like an exciting and unique landing page for people who are interested in:
1) What our ministry is about
2) When our ministry will be launching
3) Those who may want to join our launch team
4) Those who may want give financially into our vision
5) Those who want to follow us and get more information about us
I would also love for our color scheme to be reflective of our logo.
I included more detailed instructions and what we are looking for in the enclosed document
Religious/Christian

```html
<!DOCTYPE html>
<html lang="en">
<head>
<meta charset="utf-8">
<title>Kindle Fellowship Church – Coming Soon</title>
<link href="https://fonts.googleapis.com/css2?family=Montserrat:wght@600;700;800&family=Oswald:wght@300;400&family=Poppins:wght@400;500&display=swap" rel="stylesheet">
<style>
  :root {
    --sky: #cadeef;
    --wine: #8b4657;
    --wine-light: #a04e5c;
    --navy: #1c2a86;
    --digit: #4b4c95;
    --label: #f47a80;
    --white: #ffffff;
    --send: #f63d1d;
    --rule: rgba(255,255,255,0.4);
  }
  * { box-sizing: border-box; margin: 0; padding: 0; }
  html, body { width: 1200px; height: 622px; overflow: hidden; }
  body { position: relative; font-family: 'Poppins', sans-serif; background: var(--wine); }

  .site-header {
    position: absolute; left: 0; top: 0; width: 1200px; height: 129px;
    background: var(--sky);
    display: flex; align-items: center; justify-content: center; gap: 10px;
  }
  .brand-mark { width: 14px; height: 14px; background: var(--navy); }
  .brand-name {
    font-family: 'Montserrat', sans-serif; font-weight: 800; font-size: 26px;
    color: var(--navy); letter-spacing: 0.02em;
  }

  .hero {
    position: absolute; left: 0; top: 129px; width: 1200px; height: 493px;
    background: radial-gradient(ellipse 300px 420px at 50% 50%, var(--wine-light), var(--wine));
  }

  .headline {
    position: absolute; left: 0; width: 1200px; top: 196px; text-align: center;
    font-family: 'Montserrat', sans-serif; font-weight: 700; font-size: 39px;
    letter-spacing: 0.2em; color: var(--white); padding-left: 0.2em;
  }
  .launch-date {
    position: absolute; left: 0; width: 1200px; top: 251px; text-align: center;
    font-family: 'Montserrat', sans-serif; font-weight: 700; font-size: 13px;
    letter-spacing: 0.22em; color: var(--white);
  }

  .countdown { position: absolute; top: 306px; left: 0; width: 1200px; height: 130px; }
  .digit {
    position: absolute; top: 0; width: 56px; height: 85px;
    background: var(--white); border-radius: 7px; border: 1px solid #d9dbe8;
    display: flex; align-items: center; justify-content: center;
    font-family: 'Oswald', sans-serif; font-weight: 400; font-size: 52px; color: var(--digit);
  }
  .unit-label {
    position: absolute; top: 103px; transform: translateX(-50%);
    font-family: 'Montserrat', sans-serif; font-weight: 700; font-size: 13px;
    letter-spacing: 0.06em; color: var(--label);
  }

  .divider { position: absolute; left: 306px; top: 483px; width: 588px; height: 1px; background: var(--rule); }

  .signup-note {
    position: absolute; left: 0; width: 1200px; top: 508px; text-align: center;
    font-size: 10.4px; font-weight: 500; color: var(--white);
  }
  .signup-form { position: absolute; top: 539px; left: 0; width: 1200px; height: 25px; }
  .field {
    position: absolute; top: 0; width: 194px; height: 25px; background: var(--white);
    border: none; border-radius: 1px; padding: 0 9px;
    font-family: 'Poppins', sans-serif; font-size: 9.5px; color: #333;
  }
  .field::placeholder { color: #333; }
  .send-button {
    position: absolute; top: 0; left: 874px; width: 61px; height: 25px;
    background: var(--send); color: var(--white); border: none; border-radius: 2px;
    font-family: 'Poppins', sans-serif; font-weight: 500; font-size: 10px;
  }
</style>
</head>
<body>
  <header class="site-header">
    <span class="brand-mark"></span>
    <span class="brand-name">KINDLE FELLOWSHIP CHURCH</span>
  </header>

  <main class="hero" role="img" aria-label="Faded photograph of a red brick church tower under a wine-coloured overlay"></main>

  <h1 class="headline">WE ARE COMING SOON</h1>
  <p class="launch-date">SEPTEMBER 16, 2023 AT 5PM</p>

  <section class="countdown" aria-label="Countdown to launch">
    <div class="digit" style="left:307px">1</div>
    <div class="digit" style="left:369px">8</div>
    <div class="digit" style="left:431px">0</div>
    <div class="digit" style="left:507px">2</div>
    <div class="digit" style="left:569px">3</div>
    <div class="digit" style="left:645px">4</div>
    <div class="digit" style="left:707px">5</div>
    <div class="digit" style="left:776px">2</div>
    <div class="digit" style="left:838px">4</div>
    <span class="unit-label" style="left:395px">DAYS</span>
    <span class="unit-label" style="left:558px">HOURS</span>
    <span class="unit-label" style="left:695px">MINUTES</span>
    <span class="unit-label" style="left:830px">SECONDS</span>
  </section>

  <div class="divider"></div>

  <p class="signup-note">Want to get an update on progress? Please fill up the form and sent ot us.</p>
  <form class="signup-form">
    <input class="field" style="left:266px" type="text" placeholder="your name">
    <input class="field" style="left:469px" type="email" placeholder="Email">
    <input class="field" style="left:672px" type="tel" placeholder="Phone">
    <button class="send-button" type="button">Send</button>
  </form>
</body>
</html>
```